For Tolvy: Business cards, letterhead, envelopes and double sided page

For Tolvy: Previously described in email.

Business cards, letterhead, envelopes, and glossy marketing double sided page.

Industry/Entity Type

Marketing

```html
<!DOCTYPE html>
<html lang="en">
<head>
<meta charset="utf-8">
<title>Tolvy Stationery</title>
<link rel="stylesheet" href="https://fonts.googleapis.com/css2?family=Michroma&family=Quicksand:wght@500&family=EB+Garamond:wght@500&family=Oswald:wght@700&display=swap">
<style>
:root{
  --bg:#e9e6e1;
  --ink:#0b0b0b;
  --gold:#e3a54a;
  --paper:#ffffff;
  --stripe:#2c2c2c;
  --muted:#9a9a9a;
}
*{margin:0;padding:0;box-sizing:border-box}
html,body{width:1200px;height:1000px;overflow:hidden}
body{background:var(--bg);position:relative;font-family:"Quicksand",sans-serif}
.brand{font-family:"Oswald",sans-serif;font-weight:700;color:var(--gold);text-transform:uppercase;letter-spacing:1px;line-height:1}

/* envelope */
.envelope{position:absolute;left:50px;top:68px;width:513px;height:223px;background:var(--paper);box-shadow:0 2px 6px rgba(0,0,0,.25)}
.envelope-band{position:absolute;left:0;top:0;width:100%;height:33px;background:var(--ink)}
.envelope .brand{position:absolute;left:12px;top:11px;font-size:12px}
.envelope-strip{position:absolute;left:98px;top:21px;right:0;height:12px;background:var(--gold);clip-path:polygon(10px 0,100% 0,100% 100%,0 100%)}
.envelope-strip p{font-family:"EB Garamond",serif;font-size:7.2px;color:var(--ink);line-height:12px;padding-left:14px;white-space:nowrap}

/* letterhead */
.letterhead{position:absolute;left:78px;top:357px;width:459px;height:596px;background:var(--paper);box-shadow:0 2px 6px rgba(0,0,0,.25)}
.letterhead-head{position:absolute;left:0;top:0;width:100%;height:73px;background:var(--ink);border-bottom:2px solid var(--gold);display:flex;align-items:center;justify-content:center}
.letterhead-head .brand{font-size:22px;letter-spacing:3px}
.letterhead-foot{position:absolute;left:0;bottom:0;width:100%;height:20px;background:var(--ink);display:flex;justify-content:space-between;align-items:center;padding:0 12px 0 15px;font-family:"EB Garamond",serif;font-size:9.5px;color:var(--gold);white-space:nowrap}

/* business cards */
.card{position:absolute;left:819px;width:278px;height:162px;background:var(--ink);box-shadow:0 2px 6px rgba(0,0,0,.3);overflow:hidden}
.card .brand{position:absolute;left:8px;top:10px;font-size:12px}
.card-stripes{position:absolute;right:0;top:0;width:80px;height:60px}
.card-name{position:absolute;left:0;right:0;top:63px;text-align:center;font-family:"Michroma",sans-serif;font-size:7.4px;color:var(--gold);letter-spacing:.4px}
.card-title{position:absolute;left:0;right:0;top:75px;text-align:center;font-family:"Michroma",sans-serif;font-size:4.6px;color:var(--gold);letter-spacing:.3px}
.card-contact{position:absolute;font-size:5.6px;color:var(--muted);line-height:1.1}
.card-contact li{list-style:none;display:flex;align-items:flex-start;gap:4px;margin-bottom:6px}
.card-contact li.tight{margin-bottom:4px}
.card-contact svg{width:5px;height:6px;flex:none;fill:var(--gold)}
.card-personal{left:8px;top:117px}
.card-office{left:183px;top:117px}
</style>
</head>
<body>

<section class="envelope" aria-label="Envelope">
  <div class="envelope-band"></div>
  <div class="brand">Tolvy</div>
  <div class="envelope-strip"><p>117 HARLOW AVE, SUITE 402, BROOKFIELD, NY 10120 &nbsp;TEL:555-210-4800 | www.tolvy.com</p></div>
</section>

<section class="letterhead" aria-label="Letterhead">
  <header class="letterhead-head"><div class="brand">Tolvy</div></header>
  <footer class="letterhead-foot"><span>117 HARLOW AVE, SUITE 402 BROOKFIELD, NY 10120 &nbsp;TEL 555-210-4800</span><span>www.tolvy.com</span></footer>
</section>

<svg width="0" height="0" style="position:absolute">
  <defs>
    <g id="stripes"><polygon points="20,0 34,0 80,46 80,60" fill="#222"/><polygon points="38,0 48,0 80,32 80,42" fill="#2e2e2e"/><polygon points="52,0 62,0 80,18 80,28" fill="#2e2e2e"/><polygon points="66,0 76,0 80,4 80,14" fill="#2e2e2e"/></g>
    <symbol id="i-mail" viewBox="0 0 10 10"><path d="M0 2h10v6H0z M0 2l5 3.5L10 2" fill="currentColor"/></symbol>
    <symbol id="i-mobile" viewBox="0 0 10 12"><rect x="2" y="0" width="6" height="12" rx="1"/></symbol>
    <symbol id="i-pin" viewBox="0 0 10 12"><path d="M5 0a4 4 0 0 1 4 4c0 3-4 8-4 8S1 7 1 4a4 4 0 0 1 4-4z"/></symbol>
    <symbol id="i-phone" viewBox="0 0 10 10"><path d="M2 0l2 2-1 2 3 3 2-1 2 2-2 2C4 10 0 6 0 2z"/></symbol>
    <symbol id="i-web" viewBox="0 0 10 10"><circle cx="5" cy="5" r="5"/></symbol>
  </defs>
</svg>

<article class="card" style="top:18px">
  <div class="brand">Tolvy</div>
  <svg class="card-stripes" viewBox="0 0 80 60"><use href="#stripes"/></svg>
  <p class="card-name">DANA R. WHITLOW</p><p class="card-title">PRESIDENT</p>
  <ul class="card-contact card-personal"><li><svg><use href="#i-mail"/></svg>danaw@tolvy.com</li><li><svg><use href="#i-mobile"/></svg>555-318-2046</li></ul>
  <ul class="card-contact card-office"><li class="tight"><svg><use href="#i-pin"/></svg>117 Harlow Ave. Suite 402<br>Brookfield, NY 10120</li><li class="tight"><svg><use href="#i-phone"/></svg>555-210-4800</li><li class="tight"><svg><use href="#i-web"/></svg>www.tolvy.com</li></ul>
</article>

<article class="card" style="top:216px">
  <div class="brand">Tolvy</div>
  <svg class="card-stripes" viewBox="0 0 80 60"><use href="#stripes"/></svg>
  <p class="card-name">MARISA L. OKAFOR</p><p class="card-title">DIRECTOR OF OPERATIONS</p>
  <ul class="card-contact card-personal"><li><svg><use href="#i-mail"/></svg>mokafor@tolvy.com</li><li><svg><use href="#i-mobile"/></svg>555-274-9931</li></ul>
  <ul class="card-contact card-office"><li class="tight"><svg><use href="#i-pin"/></svg>117 Harlow Ave. Suite 402<br>Brookfield, NY 10120</li><li class="tight"><svg><use href="#i-phone"/></svg>555-210-4800</li><li class="tight"><svg><use href="#i-web"/></svg>www.tolvy.com</li></ul>
</article>

<article class="card" style="top:421px">
  <div class="brand">Tolvy</div>
  <svg class="card-stripes" viewBox="0 0 80 60"><use href="#stripes"/></svg>
  <p class="card-name">PETER J. HALVORSEN</p><p class="card-title">FIELD ENGINEER</p>
  <ul class="card-contact card-personal"><li><svg><use href="#i-mail"/></svg>phalvorsen@tolvy.com</li><li><svg><use href="#i-mobile"/></svg>555-467-1203</li></ul>
  <ul class="card-contact card-office"><li class="tight"><svg><use href="#i-pin"/></svg>117 Harlow Ave. Suite 402<br>Brookfield, NY 10120</li><li class="tight"><svg><use href="#i-phone"/></svg>555-210-4800</li><li class="tight"><svg><use href="#i-web"/></svg>www.tolvy.com</li></ul>
</article>

<article class="card" style="top:616px">
  <div class="brand">Tolvy</div>
  <svg class="card-stripes" viewBox="0 0 80 60"><use href="#stripes"/></svg>
  <p class="card-name">OWEN REYES</p><p class="card-title">FIELD ENGINEER</p>
  <ul class="card-contact card-personal"><li><svg><use href="#i-mail"/></svg>oreyes@tolvy.com</li><li><svg><use href="#i-mobile"/></svg>555-406-7718</li></ul>
  <ul class="card-contact card-office"><li class="tight"><svg><use href="#i-pin"/></svg>117 Harlow Ave. Suite 402<br>Brookfield, NY 10120</li><li class="tight"><svg><use href="#i-phone"/></svg>555-210-4800</li><li class="tight"><svg><use href="#i-web"/></svg>www.tolvy.com</li></ul>
</article>

<article class="card" style="top:821px">
  <div class="brand">Tolvy</div>
  <svg class="card-stripes" viewBox="0 0 80 60"><use href="#stripes"/></svg>
  <p class="card-name">COLIN ASHBY</p><p class="card-title">FIELD ENGINEER</p>
  <ul class="card-contact card-personal"><li><svg><use href="#i-mail"/></svg>cashby@tolvy.com</li><li><svg><use href="#i-mobile"/></svg>555-318-2091</li></ul>
  <ul class="card-contact card-office"><li class="tight"><svg><use href="#i-pin"/></svg>117 Harlow Ave. Suite 402<br>Brookfield, NY 10120</li><li class="tight"><svg><use href="#i-phone"/></svg>555-210-4800</li><li class="tight"><svg><use href="#i-web"/></svg>www.tolvy.com</li></ul>
</article>

</body>
</html>
```